Business card for Full Stable Works Vanhoorne

I would like to have me designed an professional business card with my existing logo for my company called : full stable works vanhoorne gcv.
I prefer a two sided business card with on the back side only the horses head and the website : fswvanhoorne-example.eu
Only one colour shouldbe all right.
The logo must appear in a nic professional way on the business card.

Other suggestion are welcome.

All copy wrights must be released by the designer after we have selected a final design.

Target Market(s)

Equestrian businesses

Industry/Entity Type

Business

Contact Information for Business Card

Gerard Vanhoorne
Title: zaakvoerder
Full Stable Works Vanhoorne GCV
Lindekouter 47
B - 9999 Voorbeeldegem
België
Phone: + 32 400 98 76 10
Mail: gerard@fswvanhoorne-example.eu

Font styles to use
Serif

Requirements
Must have
• My own logo
• See attached files
• Website: fswvanhoorne-example.eu

```html
<!DOCTYPE html>
<html lang="nl">
<head>
<meta charset="utf-8">
<title>Full Stable Works Vanhoorne – business cards</title>
<link rel="stylesheet" href="https://fonts.googleapis.com/css2?family=Tinos:wght@400;700&display=swap">
<style>
  :root {
    --stage: #3b3b3b;
    --card-light: #ffffff;
    --card-dark: #4a4a4a;
    --ink: #1e1e1e;
    --ink-soft: #555555;
    --ink-inverse: #ffffff;
    --deco-light: #ebebeb;
    --deco-dark: #555555;
  }
  * { margin: 0; padding: 0; box-sizing: border-box; }
  html, body { width: 1200px; height: 840px; overflow: hidden; }
  body {
    background: var(--stage);
    font-family: "Tinos", serif;
    position: relative;
  }
  .card {
    position: absolute;
    width: 504px;
    height: 288px;
    overflow: hidden;
  }
  .card--front { left: 352px; top: 102px; background: var(--card-light); }
  .card--back-light { left: 89px; top: 433px; background: var(--card-light); }
  .card--back-dark { left: 614px; top: 433px; background: var(--card-dark); }

  .deco {
    position: absolute;
    inset: 0;
    width: 100%;
    height: 100%;
  }

  .brand-name {
    position: absolute;
    font-family: "Tinos", serif;
    font-weight: 700;
    color: var(--ink);
    line-height: 1.05;
    white-space: nowrap;
  }
  .card--front .brand-name {
    right: 27px;
    top: 46px;
    font-size: 19px;
    text-align: right;
  }
  .card--back-light .brand-name,
  .card--back-dark .brand-name {
    left: 0; right: 0;
    top: 122px;
    font-size: 25px;
    text-align: center;
  }
  .card--back-dark .brand-name { color: var(--ink-inverse); }

  .website-spaced {
    position: absolute;
    left: 0; right: 0;
    top: 192px;
    text-align: center;
    font-size: 13px;
    letter-spacing: 0.42em;
    color: var(--ink-soft);
    white-space: nowrap;
  }
  .card--back-dark .website-spaced { color: var(--ink-inverse); }

  .holder-name {
    position: absolute;
    left: 30px;
    top: 154px;
    font-size: 19px;
    font-weight: 700;
    color: var(--ink);
    white-space: nowrap;
  }
  .address {
    position: absolute;
    left: 31px;
    top: 198px;
    font-size: 14px;
    line-height: 18.5px;
    color: var(--ink-soft);
    font-style: normal;
    white-space: nowrap;
  }
  .contact-list {
    position: absolute;
    right: 24px;
    bottom: 20px;
    list-style: none;
    font-size: 14px;
    line-height: 19px;
    color: var(--ink-soft);
    white-space: nowrap;
  }
  .contact-list li { display: flex; align-items: center; gap: 6px; }
  .contact-icon { width: 12px; height: 12px; fill: var(--ink); flex: none; }
</style>
</head>
<body>

  <section class="card card--front" aria-label="Front of business card">
    <svg class="deco" viewBox="0 0 504 288" role="img" aria-label="Faint horse head decoration">
      <defs>
        <linearGradient id="decoFadeFront" x1="0" y1="0" x2="1" y2="0">
          <stop offset="0" stop-color="var(--deco-light)" stop-opacity="1"/>
          <stop offset="1" stop-color="var(--deco-light)" stop-opacity="0"/>
        </linearGradient>
      </defs>
      <rect x="0" y="0" width="300" height="288" fill="url(#decoFadeFront)"/>
    </svg>

    <div class="brand-name">Full Stable Works Vanhoorne</div>

    <h1 class="holder-name">Gerard Vanhoorne</h1>
    <address class="address">
      Full Stable Works<br>
      Vanhoorne GCV<br>
      Lindekouter 47<br>
      B - 9999 Voorbeeldegem, België
    </address>

    <ul class="contact-list">
      <li>
        <svg class="contact-icon" viewBox="0 0 12 12" aria-hidden="true"><path d="M2.5 0.8 4.3 3 3.4 4.3c.6 1.6 1.9 2.9 3.5 3.5L8.2 7l2.2 1.8-1 2.2C5 10.7 1.3 7 .9 2.3z"/></svg>
        + 32 400 98 76 10
      </li>
      <li>
        <svg class="contact-icon" viewBox="0 0 12 12" aria-hidden="true"><path d="M0.5 2.5h11v7h-11z M0.5 2.5 6 6.5l5.5-4" fill="none" stroke="var(--ink)" stroke-width="1.2"/><path d="M0.5 2.5h11L6 6.5z"/></svg>
        gerard@fswvanhoorne-example.eu
      </li>
      <li>
        <svg class="contact-icon" viewBox="0 0 12 12" aria-hidden="true"><circle cx="6" cy="6" r="5.6"/><path d="M1 6h10M6 .6c-2 2.8-2 8 0 10.8M6 .6c2 2.8 2 8 0 10.8" fill="none" stroke="#fff" stroke-width=".8"/></svg>
        fswvanhoorne-example.eu
      </li>
    </ul>
  </section>

  <section class="card card--back-light" aria-label="Back of business card, light version">
    <svg class="deco" viewBox="0 0 504 288" role="img" aria-label="Faint horse head decoration">
      <defs>
        <radialGradient id="decoFadeLight" cx="0.5" cy="0.5" r="0.6">
          <stop offset="0" stop-color="var(--deco-light)" stop-opacity="1"/>
          <stop offset="1" stop-color="var(--deco-light)" stop-opacity="0"/>
        </radialGradient>
      </defs>
      <rect x="40" y="0" width="440" height="288" fill="url(#decoFadeLight)"/>
    </svg>
    <div class="brand-name">Full Stable Works Vanhoorne</div>
    <p class="website-spaced">fswvanhoorne-example.eu</p>
  </section>

  <section class="card card--back-dark" aria-label="Back of business card, dark version">
    <svg class="deco" viewBox="0 0 504 288" role="img" aria-label="Faint horse head decoration">
      <defs>
        <radialGradient id="decoFadeDark" cx="0.5" cy="0.5" r="0.6">
          <stop offset="0" stop-color="var(--deco-dark)" stop-opacity="1"/>
          <stop offset="1" stop-color="var(--deco-dark)" stop-opacity="0"/>
        </radialGradient>
      </defs>
      <rect x="40" y="0" width="440" height="288" fill="url(#decoFadeDark)"/>
    </svg>
    <div class="brand-name">Full Stable Works Vanhoorne</div>
    <p class="website-spaced">fswvanhoorne-example.eu</p>
  </section>

</body>
</html>
```